The Brandling Firm

We need a new design for our letterhead and envelopes. We are a personal injury and criminal defense firm so we need something modern and clean, but more on the professional/traditional side. Our new logo has two colors and is attached to the file so we need something that works well with those colors/matches the design. The following information needs to be on the letterhead:
Phone: (555) 314-2716
Fax: (555) 314-5093
Toll-Free: (800) 555-0143
Post Office Box 4372
Harrowfield, QV 29548-4372
QVHarmCounselGroup.example
MarrowvaleTrialCounsel.example

Target Market(s)

Clients, government agencies, other law firms

Industry/Entity Type

Legal

Font styles to use
Sans Serif
Other font styles liked:
• Arial

Colors

Designer to choose colors to be used in the design.

Requirements
Must have
• Must look professional and clean, modern
Nice to have
• I would like to see a design that works with the logo but does not distract from the content that will be printed on it
Should not have
• Too many colors or crazy designs.

```html
<!DOCTYPE html>
<html lang="en">
<head>
<meta charset="utf-8">
<title>The Brandling Firm – Stationery</title>
<link rel="stylesheet" href="https://fonts.googleapis.com/css2?family=Oswald:wght@500&family=PT+Sans:wght@400;700&display=swap">
<style>
  :root {
    --board: #a87c54;
    --navy: #2e3192;
    --red: #d71f26;
    --paper: #ffffff;
    --ink: #555a66;
    --label: #ffffff;
  }
  * { box-sizing: border-box; margin: 0; padding: 0; }
  html, body { width: 1200px; height: 770px; overflow: hidden; }
  body {
    background: var(--board);
    font-family: "PT Sans", Arial, sans-serif;
    position: relative;
  }
  .sheet { position: absolute; background: var(--paper); box-shadow: 2px 3px 5px rgba(0,0,0,.3); overflow: hidden; }
  .band { position: absolute; top: 0; bottom: 0; left: 0; background: var(--navy); color: #fff; }
  .brand { display: flex; align-items: center; gap: 5px; font-weight: 700; white-space: nowrap; }
  .brand-mark { display: inline-block; background: currentColor; flex: none; }
  .brand--light { color: #fff; }
  .brand--navy { color: var(--navy); }
  .option-label {
    position: absolute; font-family: "Oswald", "Arial Narrow", sans-serif; font-weight: 500;
    color: var(--label); font-size: 18px;
  }

  /* Letterhead */
  .letterhead { left: 62px; top: 79px; width: 489px; height: 633px; }
  .letterhead .band { width: 140px; }
  .letterhead .brand { position: absolute; left: 14px; top: 62px; font-size: 13px; }
  .letterhead .brand-mark { width: 8px; height: 8px; }
  .band-contact { position: absolute; left: 0; right: 0; text-align: center; font-size: 7.4px; line-height: 1.4; }
  .band-contact b { font-weight: 700; }
  .letterhead .address { top: 469px; }
  .letterhead .phones { top: 519px; line-height: 1.95; }
  .letterhead .web { top: 587px; font-weight: 700; line-height: 1.95; letter-spacing: .2px; }

  /* Business cards */
  .card { width: 202px; height: 115px; }
  .card .details { position: absolute; font-size: 4.6px; line-height: 1.75; color: var(--ink); white-space: nowrap; }
  .card .details .gap { height: 4px; }
  .card .name { font-size: 6.8px; font-weight: 700; }
  .card .role { font-size: 4.8px; }
  .card-one { left: 602px; top: 65px; }
  .card-one .name-row { position: absolute; left: 10px; top: 13px; display: flex; align-items: center; gap: 4px; }
  .card-one .name-row .rule { width: 12px; height: 3px; background: #e6e6e6; }
  .card-one .name { color: var(--navy); }
  .card-one .role { color: #888; border-left: 1px solid #aaa; padding-left: 4px; }
  .card-one .brand { position: absolute; left: 12px; top: 70px; font-size: 9px; gap: 4px; }
  .card-one .brand-mark { width: 6px; height: 6px; }
  .card-one .divider { position: absolute; left: 113px; top: 44px; width: 1px; height: 54px; background: #ddd; }
  .card-one .details { left: 121px; top: 44px; }
  .card-one .foot { position: absolute; left: 0; right: 0; bottom: 0; height: 8px; background: var(--navy); }

  .card-back { left: 826px; top: 64px; background: var(--navy); }
  .card-back .brand { position: absolute; left: 14px; top: 51px; font-size: 11px; }
  .card-back .brand-mark { width: 6px; height: 6px; }

  .card-two { left: 601px; top: 192px; }
  .card-three { left: 833px; top: 192px; }
  .card-two .band, .card-three .band { width: 113px; }
  .card-two .brand, .card-three .brand { position: absolute; left: 10px; top: 52px; font-size: 10px; }
  .card-two .brand-mark, .card-three .brand-mark { width: 6px; height: 6px; }
  .card-two .details, .card-three .details { left: 122px; top: 12px; }
  .card-two .name, .card-two .role { color: var(--red); }
  .card-three .panel { position: absolute; left: 113px; top: 0; right: 0; bottom: 0; background: var(--red); }
  .card-three .details { color: #fff; }

  /* Envelope */
  .flap { position: absolute; left: 582px; top: 379px; }
  .flap .brand { position: absolute; left: 268px; top: 24px; font-size: 12px; transform: rotate(180deg); }
  .flap .brand-mark { width: 7px; height: 7px; }
  .envelope { left: 581px; top: 458px; width: 562px; height: 252px; }
  .envelope .band { width: 132px; }
  .envelope .address { top: 115px; }
  .envelope .phones { top: 159px; line-height: 1.75; }
  .envelope .web { top: 213px; font-weight: 700; line-height: 1.75; letter-spacing: .2px; }
  .envelope .brand { position: absolute; left: 150px; top: 176px; font-size: 22px; }
  .envelope .brand-mark { width: 12px; height: 12px; }
</style>
</head>
<body>

  <!-- Letterhead -->
  <section class="sheet letterhead">
    <div class="band">
      <div class="brand brand--light"><span class="brand-mark"></span>The Brandling Firm</div>
      <p class="band-contact address">Post Office Box 4372<br>Harrowfield, QV 29548-4372</p>
      <p class="band-contact phones"><b>Phone:</b> (555) 314-2716<br><b>Fax:</b> (555) 314-5093<br><b>Toll-Free:</b> (800) 555-0143</p>
      <p class="band-contact web">QVHarmCounselGroup.example<br>MarrowvaleTrialCounsel.example</p>
    </div>
  </section>

  <!-- Business cards -->
  <h2 class="option-label" style="left:603px;top:34px;">Front Option-1</h2>
  <section class="sheet card card-one">
    <div class="name-row"><span class="rule"></span><span class="name">Your Name Here</span><span class="role">Designation</span></div>
    <div class="brand brand--navy"><span class="brand-mark"></span>The Brandling Firm</div>
    <span class="divider"></span>
    <div class="details">
      Post Office Box 4372<br>Harrowfield, QV 29548-4372
      <div class="gap"></div>
      Phone : (555) 314-2716<br>Fax : (555) 314-5093<br>Toll-Free : (800) 555-0143<br>
      QVHarmCounselGroup.example<br>MarrowvaleTrialCounsel.example
    </div>
    <span class="foot"></span>
  </section>

  <section class="sheet card card-back">
    <div class="brand brand--light"><span class="brand-mark"></span>The Brandling Firm</div>
  </section>

  <section class="sheet card card-two">
    <div class="band"><div class="brand brand--light"><span class="brand-mark"></span>The Brandling Firm</div></div>
    <div class="details">
      <div class="name">Your Name Here</div><div class="role">Designation</div>
      <div class="gap"></div>
      Post Office Box 4372<br>Harrowfield, QV 29548-4372
      <div class="gap"></div>
      Phone : (555) 314-2716<br>Fax : (555) 314-5093<br>Toll-Free : (800) 555-0143<br>
      QVHarmCounselGroup.example<br>MarrowvaleTrialCounsel.example
    </div>
  </section>
  <h2 class="option-label" style="left:602px;top:312px;">Front Option-2</h2>

  <section class="sheet card card-three">
    <div class="band"><div class="brand brand--light"><span class="brand-mark"></span>The Brandling Firm</div></div>
    <div class="panel"></div>
    <div class="details">
      <div class="name">Your Name Here</div><div class="role">Designation</div>
      <div class="gap"></div>
      Post Office Box 4372<br>Harrowfield, QV 29548-4372
      <div class="gap"></div>
      Phone : (555) 314-2716<br>Fax : (555) 314-5093<br>Toll-Free : (800) 555-0143<br>
      QVHarmCounselGroup.example<br>MarrowvaleTrialCounsel.example
    </div>
  </section>
  <h2 class="option-label" style="left:837px;top:313px;">Front Option-3</h2>

  <!-- Envelope flap -->
  <div class="flap">
    <svg width="562" height="68" viewBox="0 0 562 68" aria-hidden="true">
      <defs>
        <clipPath id="flap-shape">
          <path d="M0 64 L28 10 Q34 0 50 0 L500 0 Q516 0 522 10 L560 64 Z"/>
        </clipPath>
      </defs>
      <g clip-path="url(#flap-shape)" style="filter:drop-shadow(1px 2px 2px rgba(0,0,0,.3))">
        <rect x="0" y="0" width="562" height="68" fill="#ffffff"/>
        <rect x="0" y="0" width="131" height="68" fill="#2e3192"/>
      </g>
    </svg>
    <div class="brand brand--navy"><span class="brand-mark"></span>The Brandling Firm</div>
  </div>

  <!-- Envelope -->
  <section class="sheet envelope">
    <div class="band">
      <p class="band-contact address">Post Office Box 4372<br>Harrowfield, QV 29548-4372</p>
      <p class="band-contact phones"><b>Phone:</b> (555) 314-2716<br><b>Fax:</b> (555) 314-5093<br><b>Toll-Free:</b> (800) 555-0143</p>
      <p class="band-contact web">QVHarmCounselGroup.example<br>MarrowvaleTrialCounsel.example</p>
    </div>
    <div class="brand brand--navy"><span class="brand-mark"></span>The Brandling Firm</div>
  </section>

</body>
</html>
```